Criação de Papelaria Profissional para Educação & Cursos
" A empresa é nova. Vamos ensinar projetistas a utilizar a plataforma BIM-Kolmar. Com esse curso os profissionais ganharão em produtividade e qualidade. "

```html
<!DOCTYPE html>
<html lang="pt">
<head>
<meta charset="UTF-8">
<title>Novabim – Capa Curso de Formação BIM</title>
<link rel="stylesheet" href="https://fonts.googleapis.com/css2?family=Poppins:wght@500;600&display=swap">
<style>
  :root {
    --canvas-bg: #f4f4f2;
    --cover-dark: #1f1f1f;
    --brand-yellow: #f7c12a;
    --text-light: #ffffff;
    --sky-light: #f5f6f7;
    --sky-mid: #dfe3e7;
    --glass-blue: #8fa6bc;
    --steel-rust: #b5664a;
  }
  html, body {
    margin: 0;
    padding: 0;
    width: 1200px;
    height: 1200px;
    overflow: hidden;
    background: var(--canvas-bg);
  }
  .cover {
    position: absolute;
    left: 40px;
    top: 382px;
    width: 1120px;
    height: 436px;
    overflow: hidden;
    font-family: "Poppins", sans-serif;
    box-shadow: 0 6px 24px rgba(0,0,0,0.12);
  }
  .cover-art {
    position: absolute;
    inset: 0;
    display: block;
  }
  .brand {
    position: absolute;
    left: 68px;
    top: 62px;
    display: flex;
    align-items: center;
    gap: 18px;
  }
  .brand-mark {
    width: 34px;
    height: 34px;
    border-radius: 50%;
    background: var(--brand-yellow);
  }
  .brand-name {
    color: var(--text-light);
    font-weight: 500;
    font-size: 62px;
    line-height: 1;
    letter-spacing: 1px;
  }
  .course-title {
    position: absolute;
    left: 61px;
    top: 220px;
    margin: 0;
    color: var(--text-light);
    font-weight: 500;
    font-size: 41px;
    line-height: 54px;
  }
  .course-title .highlight {
    color: var(--brand-yellow);
  }
  .title-rule {
    position: absolute;
    left: 61px;
    top: 344px;
    width: 348px;
    height: 5px;
    background: var(--brand-yellow);
  }
</style>
</head>
<body>
  <section class="cover">
    <svg class="cover-art" viewBox="0 0 1120 436" xmlns="http://www.w3.org/2000/svg">
      <defs>
        <linearGradient id="building-tones" x1="0" y1="0" x2="1" y2="1">
          <stop offset="0" stop-color="var(--sky-light)"/>
          <stop offset="0.45" stop-color="var(--glass-blue)"/>
          <stop offset="0.75" stop-color="var(--steel-rust)"/>
          <stop offset="1" stop-color="var(--sky-mid)"/>
        </linearGradient>
      </defs>
      <rect class="cover-bg" width="1120" height="436" fill="var(--sky-light)"/>
      <g role="img" aria-label="Ilustração de edifício em construção com estrutura metálica e fachada envidraçada">
        <rect class="building-visual" x="640" y="0" width="480" height="436" fill="url(#building-tones)" opacity="0.85"/>
      </g>
      <path class="accent-swoosh" d="M640 436 C670 250 790 110 980 20 C830 130 745 280 735 436 Z" fill="var(--brand-yellow)"/>
      <path class="dark-panel" d="M0 0 H975 C820 70 700 210 680 436 H0 Z" fill="var(--cover-dark)"/>
    </svg>

    <div class="brand">
      <span class="brand-mark"></span>
      <span class="brand-name">Novabim</span>
    </div>

    <h1 class="course-title">Curso de<br>Formação <span class="highlight">BIM</span></h1>
    <div class="title-rule"></div>
  </section>
</body>
</html>
```